GUARANTEED! Simple website for independent event planner and consultant...

I need a website that is no more than 5 or 6 pages to illustrate who I am and what I can offer to groups who book hotels for meetings and conferences. I have 20 years of experience planning meetings within hotels and I am now ready to go out on my own and help clients choose venues, negotiate contracts and plan effective meetings. I will focus on clients planning meetings in the mountains of Colorado but I am willing to travel as well. I want to work with a person who is collaborative and can direct me on what they need to move the project along quickly. I already have my logo, a hosting site and work e-mail address. Also, I recently hired a photographer to do head shots. Lastly, it important for me to be able to talk on the phone or skype with this person, as needed and I must be able to make changes to my site down the road when necessary...

Target Market(s)

Corporate Groups

Industry/Entity Type

Event Planning

Coding

Coded - Design and coding required

Number of Pages Required

5+ page

Font styles to use
Sans Serif

Requirements
Must have
• About me page, event planning services offered page, task force and consulting work page, testimonials page, page for blogs, page to contact me/request a proposal. May need advice on what else I need...
Nice to have
• I want it to look sharp and professional. I want people to look at my site and know immediately that they can trust me and the work I can do.
• I don't want it to look like it is over the top as I am not a HUGE company but I do want it to be professional and easy to view and navigate.
Should not have
• Bright colors
• My logo is bright orange and black. I have also used dark grey and orange. See below:
• Orange:
• C = 0
• M = 64
• Y = 100
• K = 0
• Gray:
• C = 67
• M = 60
• Y = 59
• K = 45
• Font: Gotham Book and Gotham Bold

```html
<!DOCTYPE html>
<html lang="en">
<head>
<meta charset="utf-8">
<title>Harlow Events</title>
<link href="https://fonts.googleapis.com/css2?family=Montserrat:wght@400;500;600;700&family=Raleway:wght@400;500&display=swap" rel="stylesheet">
<style>
:root{
  --orange:#f47b20;
  --charcoal:#333333;
  --slate:#4a4a4a;
  --frame:#5a5a5a;
  --quote-bg:#e9e9e9;
  --text:#444444;
  --white:#ffffff;
  --sky-1:#f3f7fa;
  --sky-2:#e4ecf1;
}
*{box-sizing:border-box;margin:0;padding:0}
html,body{width:1081px;height:1200px;overflow:hidden}
body{position:relative;background:var(--white);font-family:"Raleway",sans-serif;color:var(--text)}
.hero-bg{position:absolute;left:0;top:0;width:1081px;height:560px;
  background:linear-gradient(160deg,#ffffff 30%,var(--sky-1) 60%,#eef3ee 85%,#fbfbf1 100%);
  -webkit-mask-image:linear-gradient(180deg,#000 85%,transparent 100%);
  mask-image:linear-gradient(180deg,#000 85%,transparent 100%)}
.portrait{position:absolute;left:636px;top:48px;width:395px;height:495px;
  border-radius:160px 160px 0 0;
  background:linear-gradient(180deg,#d9c6a4 0%,#c9a58a 25%,#2b2b2e 45%,#f0826a 62%,#26262a 100%)}
.brand{position:absolute;left:136px;display:flex;align-items:center;gap:10px;
  font-family:"Montserrat",sans-serif;font-weight:600;font-size:22px;color:var(--charcoal);line-height:1}
.brand-mark{width:12px;height:12px;background:var(--orange);flex:none}
.site-header .brand{top:78px}
.main-nav{position:absolute;left:298px;top:54px;display:flex;gap:12px;font-family:"Montserrat",sans-serif;font-weight:600;font-size:9.5px;color:var(--charcoal)}
.main-nav .active{color:var(--orange)}
.contact-line{position:absolute;left:138px;display:flex;align-items:center;gap:8px;font-family:"Montserrat",sans-serif;color:var(--charcoal)}
.contact-line.address{top:236px;font-size:12.5px;font-weight:500}
.contact-line.phone{top:256px;font-size:17px;font-weight:700}
.cta-band{position:absolute;left:0;top:327px;width:533px;height:134px;background:var(--orange);color:var(--white);
  font-family:"Montserrat",sans-serif;text-align:right;padding:42px 32px 0 0}
.cta-band .lead{font-size:12.5px;font-weight:500}
.cta-band .headline{font-size:27px;font-weight:500;margin-top:4px;letter-spacing:.3px}
.proposal-btn{position:absolute;left:533px;top:327px;width:133px;height:134px;background:var(--slate);color:var(--white);
  font-family:"Montserrat",sans-serif;font-weight:700;font-size:12px;text-align:center;line-height:1.2;padding-top:42px}
.proposal-btn svg{display:block;margin:0 auto 8px}
.welcome{position:absolute;left:224px;top:543px;width:722px;height:457px;border:2px solid var(--frame)}
.welcome h1{position:absolute;left:-79px;top:30px;background:var(--white);padding:0 4px 18px 0;
  font-family:"Montserrat",sans-serif;font-weight:500;font-size:44px;color:var(--charcoal);letter-spacing:.5px}
.welcome .intro{position:absolute;left:33px;top:95px;width:670px;font-size:10px;line-height:16.3px}
.read-more{position:absolute;left:33px;top:162px;width:96px;height:30px;background:var(--orange);color:var(--white);
  font-size:9.5px;display:flex;align-items:center;justify-content:center}
.testimonial{position:absolute;top:227px;width:187px}
.testimonial blockquote{position:relative;background:var(--quote-bg);height:125px;padding:25px 13px 0;font-size:8px;line-height:12.2px;color:var(--text);white-space:nowrap}
.testimonial blockquote::after{content:"";position:absolute;left:28px;bottom:-18px;border-top:18px solid var(--quote-bg);border-right:18px solid transparent}
.testimonial .author{display:flex;align-items:center;gap:11px;margin-top:24px;height:40px}
.avatar{width:40px;height:40px;border-radius:50%;background:linear-gradient(180deg,#cfd6dc,#8a8f96);border:1px solid #bbb}
.author .who{font-size:9.5px;color:var(--charcoal);line-height:1.1}
.author .role{display:block;color:var(--orange);font-size:8px}
.site-footer{position:absolute;left:0;top:1061px;width:1081px;height:139px;
  background:linear-gradient(100deg,transparent 0 7%,var(--sky-1) 7% 40%,var(--sky-2) 70%,#f4f7f9 100%)}
.site-footer .brand{top:48px}
.copyright{position:absolute;left:137px;top:118px;font-size:9.5px;color:var(--charcoal)}
.social{position:absolute;left:407px;top:56px;display:flex;gap:10px}
.social span{width:44px;height:44px;border:2px solid var(--orange);border-radius:50%}
.footer-contact{position:absolute;left:670px;top:41px;list-style:none;font-size:9.5px;color:var(--charcoal)}
.footer-contact li{display:flex;align-items:center;gap:12px;height:20px}
.footer-contact svg{width:11px}
</style>
</head>
<body>
<div class="hero-bg"></div>
<div class="portrait" role="img" aria-label="Head-and-shoulders photo of the event planner in a dark blazer"></div>

<header class="site-header">
  <div class="brand"><span class="brand-mark"></span>Harlow Events</div>
  <nav class="main-nav">
    <span class="active">HOME</span><span>ABOUT</span><span>SERVICES</span><span>CONSULTING</span><span>TESTIMONIALS</span><span>BLOGS</span><span>CONTACT</span>
  </nav>
</header>

<div class="contact-line address">
  <svg width="9" height="13" viewBox="0 0 10 14"><path d="M5 0a5 5 0 0 1 5 5c0 3.5-5 9-5 9S0 8.5 0 5a5 5 0 0 1 5-5z" fill="#f47b20"/><circle cx="5" cy="5" r="2" fill="#fff"/></svg>
  218 Pine Ridge Road, Denver CO 80202
</div>
<div class="contact-line phone">
  <svg width="9" height="14" viewBox="0 0 9 14"><rect x="1" y="1" width="7" height="12" rx="1.5" fill="none" stroke="#f47b20" stroke-width="1.6"/><rect x="3" y="10" width="3" height="1.2" fill="#f47b20"/></svg>
  555.014.2290
</div>

<section class="cta-band">
  <p class="lead">Looking for the Perfect Hotel Meeting Venue?</p>
  <p class="headline">LET ME HELP YOU</p>
</section>
<div class="proposal-btn">
  <svg width="28" height="21" viewBox="0 0 28 21"><rect width="28" height="21" rx="2" fill="#fff"/><path d="M1 2l13 10L27 2" fill="none" stroke="#4a4a4a" stroke-width="2"/></svg>
  REQUEST A<br>PROPOSAL
</div>

<section class="welcome">
  <h1>WELCOME</h1>
  <p class="intro">Harlow Events offer to groups who book hotels for meetings and conferences. I have 20 years of experience planning meetings<br>within hotels and I am now ready to go out on my own and help clients choose venues, negotiate contracts and plan effective meetings. I will focus<br>on clients planning meetings in the mountains of Colorado but I am willing to travel as well</p>
  <span class="read-more">read more</span>

  <article class="testimonial" style="left:33px">
    <blockquote>" Lorem ipsum dolor sit amet, consectetur<br>adipiscing elit, sed do eiusmod tempor<br>incididunt ut labore et dolore magna<br>aliqua. Ut enim ad minim veniam, quis<br>nostrud exercitation ullamco laboris<br>nisi ut aliquip ex ea commodo consequat."</blockquote>
    <div class="author"><div class="avatar" role="img" aria-label="Client portrait"></div><p class="who">Avery Lane<span class="role">Northpeak COO</span></p></div>
  </article>
  <article class="testimonial" style="left:263px">
    <blockquote>" Lorem ipsum dolor sit amet, consectetur<br>adipiscing elit, sed do eiusmod tempor<br>incididunt ut labore et dolore magna<br>aliqua. Ut enim ad minim veniam, quis<br>nostrud exercitation ullamco laboris<br>nisi ut aliquip ex ea commodo consequat."</blockquote>
    <div class="author"><div class="avatar" role="img" aria-label="Client portrait"></div><p class="who">Jonah Pierce<span class="role">Brightfield OIC</span></p></div>
  </article>
  <article class="testimonial" style="left:499px">
    <blockquote>" Lorem ipsum dolor sit amet, consectetur<br>adipiscing elit, sed do eiusmod tempor<br>incididunt ut labore et dolore magna<br>aliqua. Ut enim ad minim veniam, quis<br>nostrud exercitation ullamco laboris<br>nisi ut aliquip ex ea commodo consequat."</blockquote>
    <div class="author"><p class="who">Marco Ellis<span class="role">Summitware President</span></p></div>
  </article>
</section>

<footer class="site-footer">
  <div class="brand"><span class="brand-mark"></span>Harlow Events</div>
  <p class="copyright">© 2017 | All Rights Reserved</p>
  <div class="social" aria-label="Social links"><span></span><span></span><span></span></div>
  <ul class="footer-contact">
    <li><svg viewBox="0 0 10 14" height="12"><path d="M5 0a5 5 0 0 1 5 5c0 3.5-5 9-5 9S0 8.5 0 5a5 5 0 0 1 5-5z" fill="#f47b20"/><circle cx="5" cy="5" r="2" fill="#fff"/></svg>Harlow Events, 218 Pine Ridge Road, Denver CO 80202</li>
    <li><svg viewBox="0 0 9 14" height="11"><rect x="1" y="1" width="7" height="12" rx="1.5" fill="none" stroke="#f47b20" stroke-width="1.6"/></svg>555.014.2290</li>
    <li><svg viewBox="0 0 14 10" height="9"><rect x="1" y="1" width="12" height="8" fill="none" stroke="#f47b20" stroke-width="1.3"/><path d="M1 1l6 5 6-5" fill="none" stroke="#f47b20" stroke-width="1.3"/></svg>dana@harlowevents.example</li>
  </ul>
</footer>
</body>
</html>
```